Poster Required for Cafe to promote Catering

I would like a Poster made to advertise that our business does catering.
On the poster we would like it to say:

Did you know that Sunny Ladle does Catering?
We offer Breakfast, Lunch, Morning and Afternoon Tea Options
Come instore to enquire

At the bottom of the flyer, can you please put the contact details:
Phone 0487 602 914
Email tam@sunnyladlecanteen.com

Poster Size A3

I have attached our logo and menu's so you can get a feel for what we like.

Target Market(s)

Hospital Staff: Doctors, Nurses, Admin

Industry/Entity Type

Hospitality

Requirements
Nice to have
• Some pictures of catering. Eg. Gourmet Sandwiches, Sliders
• You could check our instagram page for ideas on what we do..
• @snyladle_qld

```html
<!DOCTYPE html>
<html lang="en">
<head>
<meta charset="utf-8">
<title>Sunny Ladle Catering Poster</title>
<link rel="stylesheet" href="https://fonts.googleapis.com/css2?family=Arvo:wght@400;700&family=Roboto+Condensed:wght@700&family=Roboto+Slab:wght@300&display=swap">
<style>
  :root {
    --cocoa: #3d2f31;
    --butter: #f8f4a3;
    --cream: #ffffff;
    --ink: #3a2c2e;
  }
  html, body {
    margin: 0;
    padding: 0;
    overflow: hidden;
    background: var(--cream);
  }
  .poster {
    position: relative;
    width: 849px;
    height: 1200px;
    overflow: hidden;
    background: var(--cocoa);
    font-family: "Arvo", serif;
  }
  .footer-band {
    position: absolute;
    left: 0; top: 1072px;
    width: 849px; height: 128px;
    background: var(--cream);
  }
  .headline { position: absolute; left: 0; top: 0; margin: 0; width: 849px; height: 490px; }
  .headline svg { display: block; }
  .headline text { font-family: "Arvo", serif; font-weight: 700; }
  .tone-butter { fill: var(--butter); }
  .tone-cream { fill: var(--cream); }

  .offer-title {
    position: absolute; left: 0; top: 514px; width: 849px;
    display: flex; justify-content: center; align-items: center; gap: 14px;
    font-family: "Roboto Condensed", sans-serif; font-weight: 700;
    font-size: 46px; color: var(--cream); line-height: 1;
  }
  .offer-title svg { display: block; }

  .divider {
    position: absolute; top: 612px; height: 305px; width: 0;
    border-left: 3px dotted var(--butter);
  }
  .icon-area {
    position: absolute; top: 640px; height: 160px;
    background: var(--butter); opacity: 0.85; border-radius: 18px;
  }
  .meal {
    position: absolute; top: 824px;
    font-family: "Roboto Condensed", sans-serif; font-weight: 700;
    color: var(--cream); text-align: center; line-height: 1;
  }
  .meal-name { font-size: 44px; }
  .meal-note { font-size: 17px; line-height: 1.45; margin-top: 8px; }

  .ribbon { position: absolute; left: 362px; top: 982px; }
  .ribbon-text {
    position: absolute; left: 362px; top: 982px; width: 426px; height: 56px;
    display: flex; align-items: center; justify-content: center;
    font-family: "Roboto Condensed", sans-serif; font-weight: 700;
    font-size: 30px; color: var(--cream);
  }

  .brand-seal {
    position: absolute; left: 68px; top: 953px;
    width: 214px; height: 214px; border-radius: 50%;
    background: var(--cocoa); border: 13px solid var(--butter);
    display: flex; align-items: center; justify-content: center;
  }
  .brand-name {
    font-family: "Arvo", serif; font-weight: 400; font-size: 28px;
    color: var(--cream); text-align: center; line-height: 1.2; letter-spacing: 3px;
  }

  .contact { position: absolute; left: 362px; display: flex; align-items: center; gap: 14px; color: var(--ink); }
  .contact-phone { top: 1080px; }
  .contact-phone .value { font-family: "Roboto Condensed", sans-serif; font-weight: 700; font-size: 58px; line-height: 1; letter-spacing: 2px; }
  .contact-email { top: 1144px; }
  .contact-email .value { font-family: "Roboto Slab", serif; font-weight: 300; font-size: 24px; line-height: 1; }
</style>
</head>
<body>
<main class="poster">
  <div class="footer-band"></div>

  <h1 class="headline">
    <svg width="849" height="490" viewBox="0 0 849 490">
      <text x="92" y="118" font-size="56" textLength="608" lengthAdjust="spacingAndGlyphs"><tspan class="tone-butter">DID YOU KNOW </tspan><tspan class="tone-cream">THE</tspan></text>
      <text class="tone-cream" x="92" y="232" font-size="128">SUNNY</text>
      <text class="tone-cream" x="92" y="342" font-size="128">LADLE<tspan font-size="54" dx="8">DOES</tspan></text>
      <text class="tone-butter" x="92" y="462" font-size="128" textLength="668" lengthAdjust="spacingAndGlyphs">CATERING?</text>
    </svg>
  </h1>

  <div class="offer-title">
    <svg width="52" height="34" viewBox="0 0 52 34" aria-hidden="true">
      <rect x="0" y="0" width="52" height="6" fill="var(--butter)"/>
      <rect x="0" y="14" width="52" height="6" fill="var(--butter)"/>
      <rect x="0" y="28" width="52" height="6" fill="var(--butter)"/>
    </svg>
    <span>WE OFFER</span>
    <svg width="52" height="34" viewBox="0 0 52 34" aria-hidden="true">
      <rect x="0" y="0" width="52" height="6" fill="var(--butter)"/>
      <rect x="0" y="14" width="52" height="6" fill="var(--butter)"/>
      <rect x="0" y="28" width="52" height="6" fill="var(--butter)"/>
    </svg>
  </div>

  <div class="divider" style="left:306px"></div>
  <div class="divider" style="left:554px"></div>

  <div class="icon-area" style="left:92px;width:160px" role="img" aria-label="Sandwich icon for breakfast"></div>
  <div class="icon-area" style="left:345px;width:170px" role="img" aria-label="Serving cloche with a plated meal icon for lunch"></div>
  <div class="icon-area" style="left:605px;width:150px" role="img" aria-label="Steaming teacup with tea bag icon for tea"></div>

  <div class="meal" style="left:62px;width:214px"><div class="meal-name">BREAKFAST</div></div>
  <div class="meal" style="left:326px;width:196px"><div class="meal-name">LUNCH</div></div>
  <div class="meal" style="left:582px;width:196px">
    <div class="meal-name">TEA</div>
    <div class="meal-note">MORNING &amp;<br>AFTERNOON OPTIONS</div>
  </div>

  <svg class="ribbon" width="426" height="56" viewBox="0 0 426 56" aria-hidden="true">
    <polygon points="2,2 424,2 404,28 424,54 2,54 22,28" fill="none" stroke="var(--butter)" stroke-width="3"/>
  </svg>
  <div class="ribbon-text">COME INSTORE TO ENQUIRE</div>

  <div class="brand-seal">
    <div class="brand-name">SUNNY<br>LADLE</div>
  </div>

  <div class="contact contact-phone">
    <svg width="44" height="44" viewBox="0 0 44 44" aria-hidden="true">
      <circle cx="22" cy="22" r="19" fill="none" stroke="var(--ink)" stroke-width="3"/>
      <path d="M16 11 h5 l2 6 -3 2 c1 3 3 5 6 6 l2 -3 6 2 v5 c0 2 -2 3 -4 3 c-9 -1 -16 -8 -17 -17 c0 -2 1 -4 3 -4 z" fill="var(--ink)"/>
    </svg>
    <span class="value">0487 602 914</span>
  </div>

  <div class="contact contact-email">
    <svg width="44" height="30" viewBox="0 0 44 30" aria-hidden="true">
      <path d="M3 10 L22 2 L41 10 V28 H3 Z" fill="none" stroke="var(--ink)" stroke-width="3" stroke-linejoin="round"/>
      <path d="M3 10 L22 21 L41 10" fill="none" stroke="var(--ink)" stroke-width="3" stroke-linejoin="round"/>
    </svg>
    <span class="value">tam@sunnyladlecanteen.com</span>
  </div>
</main>
</body>
</html>
```